UI/ UX Design for ERP Software

We need a new UX/UI interface for a ERP software for property managers. Our CMMS / ERP solution is made based on responsive design technologies and is coded in PHP.
The overall UX to be similar to Zel Kavo - easy navigation, intuitive menus.

Industry/Entity Type

Property Management

Number of Pages Required

5+ page

Requirements
Must have
• Round dock buttons
Consistent icons across the application
Enough Spacing between buttons/icons/ menu
Consistent Font
Nice to have
• We would like the UX to allow the users to use the application without /minimum training.
Should not have
• we don't want anything that is classic with respect to UX

```html
<!DOCTYPE html>
<html lang="en">
<head>
<meta charset="utf-8">
<title>Estatly Dashboard</title>
<link href="https://fonts.googleapis.com/css2?family=Mulish:wght@400;600;700&family=Saira+Condensed:wght@300;400&display=swap" rel="stylesheet">
<style>
:root{
  --bg:#eef0f3;
  --panel:#f6f7f9;
  --white:#ffffff;
  --ink:#2a2d33;
  --muted:#585d66;
  --blue:#0a6cf0;
  --line:#d8dce2;
  --footer:#4f6179;
  --c-users:#1a7ff5;
  --c-props:#e0605d;
  --c-maint:#5fa4d9;
  --c-orders:#2533c9;
  --c-reports:#c55ddb;
  --c-files:#7b4cf0;
  --c-pages:#8e6a3e;
  --c-config:#eeb50c;
  --c-tenant:#e39a62;
  --c-settings:#20c35a;
}
*{box-sizing:border-box;margin:0;padding:0}
html,body{width:1200px;height:817px;overflow:hidden}
body{position:relative;background:linear-gradient(160deg,#f7f8fa 0%,var(--bg) 60%,#f1f2f5 100%);font-family:"Mulish",sans-serif;color:var(--ink)}
.topbar{position:absolute;left:0;top:0;width:1200px;height:145px;background:#f7f8fa;border-bottom:1px solid var(--line)}
.brand{position:absolute;left:32px;top:18px;display:flex;align-items:center;gap:8px;font-weight:700;font-size:30px;color:var(--blue)}
.brand-mark{width:22px;height:22px;background:var(--blue);border-radius:4px}
.welcome{position:absolute;left:264px;top:23px;font-size:12px;color:var(--ink)}
.welcome span{color:var(--blue)}
.search{position:absolute;left:498px;top:15px;width:329px;height:29px;border:1px solid #e2e5ea;border-radius:15px;background:var(--white);font-size:10px;color:#555;padding:9px 20px}
.search svg{position:absolute;right:14px;top:8px}
.user{position:absolute;left:966px;top:16px;display:flex;align-items:center;gap:8px;font-size:12px}
.avatar{width:27px;height:27px;border-radius:50%;background:linear-gradient(#c9a58c,#6b4a3a)}
.power{position:absolute;left:1158px;top:23px}
.stat{position:absolute;top:71px;width:204px;height:51px;background:var(--white);box-shadow:0 2px 6px rgba(0,0,0,.05);padding:8px 14px;overflow:hidden}
.stat-label{font-size:11px;color:var(--ink)}
.stat-value{font-family:"Saira Condensed",sans-serif;font-weight:300;font-size:22px;color:var(--blue);line-height:1.05}
.stat svg{position:absolute;right:0;top:18px;opacity:.12}
.dock{position:absolute;left:30px;width:1140px;display:flex}
.dock-item{position:relative;width:204px;margin-right:30px;height:126px;display:flex;flex-direction:column;align-items:center;padding-top:22px}
.dock-item:last-child{margin-right:0}
.dock-item.active{background:var(--white);border-radius:6px;box-shadow:0 4px 14px rgba(0,0,0,.06)}
.dock-item.active::after{content:"";position:absolute;bottom:-6px;left:96px;border:6px solid transparent;border-top-color:var(--white);border-bottom:0}
.dock-icon{width:60px;height:60px;border-radius:6px;display:flex;align-items:center;justify-content:center;box-shadow:0 4px 10px rgba(0,0,0,.12)}
.dock-label{margin-top:18px;font-size:13px;font-weight:700;color:var(--muted)}
.dock.top{top:170px}
.dock.bottom{top:587px}
.assigned{position:absolute;left:30px;top:327px;width:1140px;height:230px;background:var(--panel);border-radius:6px;box-shadow:0 2px 10px rgba(0,0,0,.04)}
.assigned h2{position:absolute;left:30px;top:30px;font-weight:400;font-size:24px}
.btn{position:absolute;right:30px;top:30px;width:148px;height:29px;border-radius:15px;background:var(--blue);color:var(--white);font-size:11px;font-weight:700;display:flex;align-items:center;justify-content:center}
.property{position:absolute;top:88px;display:flex;align-items:center;gap:15px}
.property-photo{width:111px;height:111px;border-radius:3px;background:linear-gradient(180deg,#3a66a8 0%,#6d7f98 40%,#9c8c78 70%,#2e3a30 100%)}
.property-name{font-size:14px;font-weight:600;line-height:1.2}
.property-name span{display:block;color:var(--blue)}
footer{position:absolute;left:0;top:788px;width:1200px;height:29px;background:var(--footer);color:var(--white);font-size:10px;padding:8px 30px}
</style>
</head>
<body>
<header class="topbar">
  <div class="brand"><span class="brand-mark"></span>Estatly</div>
  <div class="welcome">Welcome to <span>Estatly</span></div>
  <div class="search">Search Asset ...
    <svg width="11" height="11" viewBox="0 0 12 12" fill="none" stroke="#999" stroke-width="1.5"><circle cx="5" cy="5" r="4"/><path d="M8 8l3 3"/></svg>
  </div>
  <div class="user"><span class="avatar" role="img" aria-label="User avatar"></span>Welcome Leon
    <svg width="9" height="6" viewBox="0 0 9 6" fill="none" stroke="#333" stroke-width="1.5"><path d="M1 1l3.5 3.5L8 1"/></svg></div>
  <svg class="power" width="12" height="12" viewBox="0 0 12 12" fill="none" stroke="#333" stroke-width="1.5"><path d="M3.5 3a4.5 4.5 0 1 0 5 0M6 1v5"/></svg>

  <div class="stat" style="left:30px"><div class="stat-label">Properties</div><div class="stat-value">03</div>
    <svg width="44" height="36" viewBox="0 0 44 36"><path d="M22 2L2 20h6v16h28V20h6z" fill="#000"/></svg></div>
  <div class="stat" style="left:264px"><div class="stat-label">Tenants</div><div class="stat-value">08</div>
    <svg width="46" height="34" viewBox="0 0 46 34" fill="#000"><circle cx="23" cy="8" r="7"/><circle cx="9" cy="12" r="5"/><circle cx="37" cy="12" r="5"/><path d="M10 34c0-12 26-12 26 0zM0 32c0-8 14-9 14 0zM32 32c0-9 14-8 14 0z"/></svg></div>
  <div class="stat" style="left:498px"><div class="stat-label">Total Properties Area</div><div class="stat-value">422,000.00 SQ.FT.</div>
    <svg width="32" height="32" viewBox="0 0 32 32" fill="none" stroke="#000" stroke-width="6"><path d="M2 12V2h10M20 2h10v10M30 20v10H20M12 30H2V20"/></svg></div>
  <div class="stat" style="left:732px"><div class="stat-label">Rented Area</div><div class="stat-value">233,500.00 SQ.FT.</div>
    <svg width="32" height="32" viewBox="0 0 32 32" fill="none" stroke="#000" stroke-width="6"><path d="M2 12V2h10M20 2h10v10M30 20v10H20M12 30H2V20M6 6l20 20M26 6L6 26"/></svg></div>
  <div class="stat" style="left:966px"><div class="stat-label">Vacancies Area</div><div class="stat-value">188,500.00</div>
    <svg width="32" height="32" viewBox="0 0 32 32" fill="none" stroke="#000" stroke-width="6"><path d="M2 12V2h10M20 2h10v10M30 20v10H20M12 30H2V20"/></svg></div>
</header>

<nav class="dock top">
  <div class="dock-item"><div class="dock-icon" style="background:var(--c-users)">
    <svg width="40" height="30" viewBox="0 0 40 30" fill="none" stroke="#fff" stroke-width="1.8"><circle cx="20" cy="9" r="5"/><circle cx="9" cy="11" r="4"/><circle cx="31" cy="11" r="4"/><path d="M11 28c0-10 18-10 18 0zM2 24c0-7 10-7 10-3M38 24c0-7-10-7-10-3"/></svg></div><div class="dock-label">Users</div></div>
  <div class="dock-item active"><div class="dock-icon" style="background:var(--c-props)">
    <svg width="34" height="36" viewBox="0 0 34 36" fill="none" stroke="#fff" stroke-width="1.5"><rect x="7" y="3" width="20" height="31"/><path d="M11 8h3M16 8h3M21 8h2M11 13h3M16 13h3M21 13h2M11 18h3M16 18h3M21 18h2M14 34v-8h6v8M1 34h32"/><circle cx="3.5" cy="27" r="2.5"/><circle cx="30.5" cy="27" r="2.5"/></svg></div><div class="dock-label">Properties</div></div>
  <div class="dock-item"><div class="dock-icon" style="background:var(--c-maint)">
    <svg width="36" height="36" viewBox="0 0 36 36" fill="none" stroke="#fff" stroke-width="1.6"><path d="M12 10a8 8 0 0 1 16 0zM10 10h20"/><circle cx="14" cy="24" r="4"/><circle cx="14" cy="24" r="8" stroke-dasharray="3 2"/><circle cx="28" cy="20" r="4" stroke-dasharray="2 1.5"/></svg></div><div class="dock-label">Prevent. Maintenance</div></div>
  <div class="dock-item"><div class="dock-icon" style="background:var(--c-orders)">
    <svg width="32" height="36" viewBox="0 0 32 36" fill="none" stroke="#fff" stroke-width="1.6"><rect x="3" y="2" width="20" height="26"/><path d="M7 8h12M7 13h12M7 18h8M17 34v-14a2 2 0 0 1 4 0v8h6v6"/></svg></div><div class="dock-label">Orders</div></div>
  <div class="dock-item"><div class="dock-icon" style="background:var(--c-reports)">
    <svg width="30" height="36" viewBox="0 0 30 36" fill="none" stroke="#fff" stroke-width="1.6"><rect x="3" y="2" width="24" height="32"/><path d="M7 9l2 2 3-3M14 10h9M7 17l2 2 3-3M14 18h9M7 25l2 2 3-3M14 26h9"/></svg></div><div class="dock-label">Reports</div></div>
</nav>

<section class="assigned">
  <h2>Assigned Properties</h2>
  <div class="btn">View All Properties</div>
  <div class="property" style="left:30px"><div class="property-photo" role="img" aria-label="Modern villa exterior at dusk"></div><div class="property-name">Lorem Ipsum is<span>Property-01</span></div></div>
  <div class="property" style="left:315px"><div class="property-photo" role="img" aria-label="Modern villa exterior at dusk"></div><div class="property-name">Lorem Ipsum is<span>Property-02</span></div></div>
  <div class="property" style="left:599px"><div class="property-photo" role="img" aria-label="Modern villa exterior at dusk"></div><div class="property-name">Lorem Ipsum is<span>Property-03</span></div></div>
  <div class="property" style="left:883px"><div class="property-photo" role="img" aria-label="Modern villa exterior at dusk"></div><div class="property-name">Lorem Ipsum is<span>Property-04</span></div></div>
</section>

<nav class="dock bottom">
  <div class="dock-item"><div class="dock-icon" style="background:var(--c-files)">
    <svg width="36" height="34" viewBox="0 0 36 34" fill="none" stroke="#fff" stroke-width="1.6"><path d="M4 8l10-3 6 22-10 3z"/><rect x="14" y="3" width="18" height="24"/><path d="M18 9h10M18 13h10M18 17h10M18 21h10"/></svg></div><div class="dock-label">Files</div></div>
  <div class="dock-item"><div class="dock-icon" style="background:var(--c-pages)">
    <svg width="36" height="34" viewBox="0 0 36 34" fill="none" stroke="#fff" stroke-width="1.6"><rect x="2" y="2" width="26" height="24"/><path d="M2 7h26M6 12h12M6 17h8"/><rect x="14" y="14" width="18" height="16" fill="var(--c-pages)"/><path d="M18 20h10M18 25h10"/></svg></div><div class="dock-label">Pages</div></div>
  <div class="dock-item"><div class="dock-icon" style="background:var(--c-config)">
    <svg width="36" height="36" viewBox="0 0 36 36" fill="none" stroke="#fff" stroke-width="1.6"><rect x="22" y="3" width="8" height="8"/><rect x="4" y="25" width="8" height="8"/><circle cx="18" cy="18" r="4"/><path d="M26 11v4l-5 1M8 25v-4l6-2M12 29h10M30 11v14"/></svg></div><div class="dock-label">Configurations</div></div>
  <div class="dock-item"><div class="dock-icon" style="background:var(--c-tenant)">
    <svg width="36" height="34" viewBox="0 0 36 34" fill="none" stroke="#fff" stroke-width="1.6"><path d="M3 14v18h30V14L18 4z"/><path d="M3 14l15 11 15-11M3 32l11-9M33 32l-11-9"/><path d="M15 11a3 3 0 1 1 4 3v2M18 19v1"/></svg></div><div class="dock-label">Tenant Requests</div></div>
  <div class="dock-item"><div class="dock-icon" style="background:var(--c-settings)">
    <svg width="38" height="36" viewBox="0 0 38 36" fill="none" stroke="#fff" stroke-width="1.6"><circle cx="19" cy="9" r="3"/><circle cx="19" cy="9" r="6" stroke-dasharray="3 2"/><circle cx="9" cy="22" r="3"/><circle cx="9" cy="22" r="6" stroke-dasharray="3 2"/><circle cx="28" cy="24" r="7" stroke-dasharray="3 2"/><path d="M25 24h1M28 24h1M31 24h1"/></svg></div><div class="dock-label">Settings</div></div>
</nav>

<footer>© 2021 Estatly. All Rights Reserved</footer>
</body>
</html>
```